Harborline Tech Service, Technology & Security Co.

need a new business card design for our Technology & Security Company. We are a Computer Networking Company, Security Camera Installers, Phone Systems.

Target Market(s)

Construction, Medical, Law Offices, Accounting, Retail etc.

Industry/Entity Type

Information Technology

Contact Information for Business Card

Logo is attached, colors are Blue, Red, Black. Blue for Technology & Red is for Security Cameras, Access Control, Alarm Systems

Colors
fbed22
ec1f27
0555a3
ffffff

Requirements
Must have
• Pictures or Icons for
• For Technology:
• Computer, Network, Phone System, Copier, TV, Cabling
• For Security:
• Video Surveillance, Access Control, Intercom, Fire Alarm, Burglar Alarm, Time Clock

```html
<!DOCTYPE html>
<html lang="en">
<head>
<meta charset="utf-8">
<title>Harborline Tech Service – Business Card</title>
<link href="https://fonts.googleapis.com/css2?family=Open+Sans:wght@400;600;700;800&family=Roboto:wght@400;700&display=swap" rel="stylesheet">
<style>
  :root {
    --backdrop: #1f1f1f;
    --paper: #ffffff;
    --brand-blue: #0a70b8;
    --accent-blue: #0555a3;
    --accent-red: #ec1f27;
    --ink: #1b1b1b;
    --muted: #555555;
  }
  * { margin: 0; padding: 0; box-sizing: border-box; }
  html, body { width: 1200px; height: 960px; overflow: hidden; }
  body {
    background: var(--backdrop);
    font-family: "Open Sans", Arial, sans-serif;
    position: relative;
  }
  .card {
    position: absolute;
    width: 600px;
    height: 343px;
  }
  .card--front { left: 314px; top: 113px; background: var(--paper); }
  .card--back { left: 311px; top: 472px; background: var(--brand-blue); color: #fff; text-align: center; }

  .wordmark {
    position: absolute;
    left: 0; right: 0;
    display: flex;
    flex-direction: column;
    align-items: center;
  }
  .wordmark__name {
    display: flex;
    align-items: center;
    gap: 10px;
    font-weight: 800;
    font-size: 27px;
    letter-spacing: -0.5px;
    line-height: 1;
  }
  .wordmark__square { width: 14px; height: 14px; }
  .wordmark__tagline {
    margin-top: 6px;
    font-size: 15px;
    font-weight: 600;
    line-height: 1;
  }
  .card--front .wordmark { top: 72px; }
  .card--front .wordmark__name { color: var(--ink); }
  .card--front .wordmark__square { background: var(--accent-red); }
  .card--front .wordmark__tagline { color: var(--muted); }
  .card--back .wordmark { top: 82px; }
  .card--back .wordmark__name { color: #fff; }
  .card--back .wordmark__square { background: #fff; }
  .card--back .wordmark__tagline { color: #fff; }

  .edge-bar { position: absolute; width: 10px; }
  .edge-bar--left { left: 0; top: 217px; height: 76px; background: var(--accent-blue); }
  .edge-bar--right { right: 0; top: 222px; height: 76px; background: var(--accent-red); }

  .person { position: absolute; left: 31px; top: 214px; }
  .person__name { color: var(--accent-blue); font-weight: 700; font-size: 20px; line-height: 24px; }
  .person__role { color: var(--accent-red); font-size: 15px; line-height: 20px; }
  .person__address { color: var(--muted); font-size: 15px; line-height: 20px; margin-top: 4px; }

  .contacts { position: absolute; right: 31px; top: 222px; list-style: none; }
  .contacts li {
    display: flex; justify-content: flex-end; align-items: center; gap: 9px;
    color: var(--muted); font-size: 15px; line-height: 19.5px;
  }
  .contacts svg { width: 13px; height: 13px; fill: var(--accent-blue); }

  .services { position: absolute; left: 0; right: 0; top: 164px; font-family: "Roboto", Arial, sans-serif; }
  .services__group + .services__group { margin-top: 12px; }
  .services__title { font-family: "Open Sans", Arial, sans-serif; font-weight: 700; font-size: 15px; line-height: 20px; }
  .services__list { font-size: 14.5px; line-height: 18px; }
</style>
</head>
<body>
  <section class="card card--front" aria-label="Business card front">
    <div class="wordmark">
      <div class="wordmark__name"><span>HARBORLINE TECH SERVICE</span><span class="wordmark__square"></span></div>
      <div class="wordmark__tagline">Technology &amp; Security Co.</div>
    </div>
    <span class="edge-bar edge-bar--left"></span>
    <span class="edge-bar edge-bar--right"></span>
    <div class="person">
      <div class="person__name">DANIEL REYES</div>
      <div class="person__role">CEO/FOUNDER</div>
      <div class="person__address">4120 Willow Crest Drive<br>Fairbanks, Alaska 99701</div>
    </div>
    <ul class="contacts">
      <li>555 210 4861
        <svg viewBox="0 0 16 16" aria-hidden="true"><path d="M1 6c0-2 3-4 7-4s7 2 7 4v1h-4V5.5H5V7H1z"/><path d="M3 8h10l1 6H2z"/></svg></li>
      <li>555 374 9026
        <svg viewBox="0 0 16 16" aria-hidden="true"><path d="M4 0h8a1 1 0 0 1 1 1v14a1 1 0 0 1-1 1H4a1 1 0 0 1-1-1V1a1 1 0 0 1 1-1zm1 2v10h6V2zm3 11a1 1 0 1 0 0 2 1 1 0 0 0 0-2z"/></svg></li>
      <li>555 618 3375
        <svg viewBox="0 0 16 16" aria-hidden="true"><path d="M4 1h8v4H4z"/><path d="M1 6h14v7H1zm3 3v1h8V9z"/><path d="M4 13h8v2H4z"/></svg></li>
      <li>dan@HarborlineTech.com
        <svg viewBox="0 0 16 16" aria-hidden="true"><path d="M1 3h14v1.5L8 9 1 4.5z"/><path d="M1 6.3l7 4.5 7-4.5V13H1z"/></svg></li>
    </ul>
  </section>

  <section class="card card--back" aria-label="Business card back">
    <div class="wordmark">
      <div class="wordmark__name"><span>HARBORLINE TECH SERVICE</span><span class="wordmark__square"></span></div>
      <div class="wordmark__tagline">Technology &amp; Security Co.</div>
    </div>
    <div class="services">
      <div class="services__group">
        <div class="services__title">FOR TECHNOLOGY</div>
        <div class="services__list">Computer • Network • Phone System<br>Copier • TV • Cabling</div>
      </div>
      <div class="services__group">
        <div class="services__title">FOR SECURITY</div>
        <div class="services__list">Video Surveillance • Access Control • Intercom<br>Fire Alarm • Burglar Alarm • Time Clock</div>
      </div>
    </div>
  </section>
</body>
</html>
```